High-end Oceanfront Real Estate Group Needs Clean, Modern Web Design

I’m looking for a clean, professional, modern and beautiful homepage web design for a Real Estate group in Southern California, USA.

The group/company is “Marlow on the Shore,” and they specialize in high end (i.e. expensive), oceanfront real estate in the Orange County area.

The look and feel of the page should accentuate the brand qualities: luxurious/expensive, professional, and beautiful (Orange County is one of the most beautiful areas in all the US and we would love the site to emphasize the beautiful beaches and scenery it has to offer).

Looks we like:
• www.brantleyhomesrealty.example
• www.keptbyfenwick.example -- I think the design is pretty out-dated in this site, but I like the organization/layout of the site

Header Tags (I don’t know if we can fit all of these, may need a side-menu, but I’d prefer header title only if possible):
• Welcome
• Featured Listings
• Previously Sold
• Sell
• Property Search
• Team
• Videos
• Blog
• Explore O.C.
• Contact

I have attached the beach and logo pics that we would like to use as the header, a few pictures of the team, and one sample home/view pic which can be used in any of the other sections (for pictures of the homes, just find expensive oceanfront houses and that will be fine).

I promise to provide feedback to each and every design submission. I appreciate the hard work that all of you are putting into your designs. There can be only one contest winner, but I hope to give all of you helpful feedback to submit the best designs possible!

Target Market(s)

Very wealthy home owners of oceanfront properties. These properties are worth several millions of dollars, and thus the site and brand needs to be targeted to very wealthy, successful individuals and families (both US and international buyers).

Industry/Entity Type

Real Estate

Number of Pages Required

2 page

Requirements
Must have
• I don’t want to give too many requirements, because I want to let you all be creative. However, here are the few Must Haves:
• Must submit 2 page designs (a home page and a sub page)
• Must use logo provided
• Focus is mostly on homes, but I would like to include some beach/ocean imagery as well
• The first “item” on the home page should be an accordion/slider which shows pictures of homes and with 1 line of text: “List with the Leader” and two link buttons: “Sell Your Home” and “Buy Your Home”
• Color palette needs to be mainly blues--to match ocean and sky blue
• Exported in all major formats (psd,ai,eps,png,jpeg,etc)
Nice to have
• We don’t necessarily need all of these, but would like to feature most:
• List of videos
• “Meet the Team”—brief team bios and pics
• Link(s) to Blog
• “List with the Leader” – section on why they should choose this firm
• Featured Listings
• Previously Sold

```html
<!DOCTYPE html>
<html lang="en">
<head>
<meta charset="utf-8">
<title>Marlow on the Shore — Oceanfront Real Estate</title>
<link href="https://fonts.googleapis.com/css2?family=Lato:wght@300;400;700&display=swap" rel="stylesheet">
<style>
:root{
  --blue:#1f6fb2;
  --blue-dark:#15558c;
  --blue-soft:#3c8ad0;
  --ink:#3d4450;
  --muted:#7c8590;
  --light:#f3f4f6;
  --white:#ffffff;
  --navy:#0d1b33;
  --navy-2:#14284a;
}
*{box-sizing:border-box;margin:0;padding:0}
html,body{width:1200px;height:3493px;overflow:hidden}
body{font-family:"Lato",Arial,sans-serif;color:var(--ink);background:var(--white);position:relative}
section,header,footer{position:absolute;left:0;width:1200px}
.photo{position:absolute;display:block}

/* nav + hero */
.hero{top:0;height:616px}
.hero-photo{inset:0;background:linear-gradient(180deg,#9fc3e6 0%,#c9dcec 14%,#4f7a3e 36%,#6b8f4a 55%,#cdd2cf 72%,#8a9aa4 100%)}
.main-nav{position:absolute;top:0;left:0;width:1200px;height:62px;background:rgba(255,255,255,.82);display:flex;justify-content:center;align-items:center;gap:0}
.main-nav a{font-size:11.5px;font-weight:700;letter-spacing:.4px;color:#3a4657;text-decoration:none;padding:0 17px;line-height:62px;text-transform:uppercase}
.main-nav a.active{color:var(--blue);border-bottom:2px solid var(--blue);line-height:58px}
.main-nav svg{margin-left:12px}
.brand-panel{position:absolute;left:87px;top:112px;width:375px;height:390px;background:rgba(255,255,255,.62)}
.brand-name{position:absolute;left:30px;top:50px;width:320px;font-size:56px;font-weight:300;color:#3a4250;line-height:1.05;letter-spacing:3px;text-transform:uppercase}
.brand-tag{position:absolute;left:87px;top:410px;width:375px;height:92px;background:rgba(31,111,178,.55);color:var(--white);font-size:28px;font-weight:400;letter-spacing:1px;padding:26px 22px;text-transform:uppercase}
.hero-btn{position:absolute;top:516px;height:55px;width:180px;font-size:13px;font-weight:700;color:var(--white);text-transform:uppercase;display:flex;align-items:center;justify-content:center;letter-spacing:.4px}
.hero-btn.outline{left:87px;border:1px solid rgba(255,255,255,.85);background:rgba(0,0,0,.15)}
.hero-btn.solid{left:272px;background:var(--blue)}
.hero-arrow{position:absolute;top:180px;left:475px}
.hero-dots{position:absolute;right:80px;top:140px;display:flex;flex-direction:column;gap:10px}
.hero-dots span{width:10px;height:10px;border-radius:50%;background:rgba(255,255,255,.8)}

/* intro */
.intro{top:616px;height:407px;text-align:center}
.section-title{font-size:31px;font-weight:300;letter-spacing:1px;text-transform:uppercase}
.intro .section-title{color:var(--blue);margin-top:62px}
.intro p{font-size:13px;line-height:24px;color:#555c66;width:1030px;margin:22px auto 0}
.intro p+p{margin-top:14px}
.btn{position:absolute;height:40px;font-size:13px;font-weight:700;text-transform:uppercase;display:flex;align-items:center;justify-content:center;letter-spacing:.4px}
.btn.outline{border:1px solid var(--blue);color:var(--blue);background:var(--white)}
.btn.solid{background:var(--blue);color:var(--white)}

/* videos */
.videos{top:1023px;height:516px}
.videos-bg{inset:0;background:linear-gradient(180deg,#8fb0cf 0%,#3a6ea6 30%,#1f4f8a 65%,#2a5f99 100%)}
.videos .section-title{position:absolute;top:68px;width:100%;text-align:center;color:var(--white)}
.video{position:absolute;border:3px solid rgba(255,255,255,.85)}
.video svg{position:absolute;left:50%;top:50%;transform:translate(-50%,-50%)}
.side-arrow{position:absolute}

/* team */
.team{top:1539px;height:337px;background:var(--light);text-align:center}
.team .section-title{color:var(--blue);margin-top:62px}
.member{position:absolute;border-radius:50%;border:3px solid var(--white);box-shadow:0 2px 6px rgba(0,0,0,.15)}
.member-name{position:absolute;left:574px;width:200px;top:284px;text-align:center}
.member-name strong{display:block;font-size:12px;color:var(--blue);text-transform:uppercase;letter-spacing:.3px}
.member-name span{font-size:11.5px;color:var(--muted)}

/* listings */
.listings{top:1876px;height:769px;text-align:center}
.listings .section-title{color:#555c66;margin-top:68px}
.card{position:absolute;width:260px;height:255px}
.card .photo{left:0;top:0;width:260px;height:180px}
.card .cap{position:absolute;top:180px;left:0;width:260px;height:75px;padding-top:18px;text-align:center}
.cap strong{display:block;font-size:12px;color:#444b55;text-transform:uppercase;font-weight:700}
.cap span{font-size:11.5px;color:#8a929b}
.card.active .cap{background:var(--blue)}
.card.active .cap strong,.card.active .cap span{color:var(--white)}
.zoom{position:absolute;left:115px;top:75px}

/* sold */
.sold{top:2645px;height:449px;background:var(--light);text-align:center}
.sold .section-title{color:#555c66;margin-top:60px}
.sold p{font-size:13px;line-height:24px;color:#555c66;width:1030px;margin:8px auto 0}
.sold-item{position:absolute;top:182px;width:253px;height:177px}
.sold-over{position:absolute;right:18px;bottom:14px;text-align:right;color:var(--white)}
.sold-over strong{display:block;font-size:17px;text-transform:uppercase;font-weight:700}
.sold-over span{font-size:11px;text-transform:uppercase;font-weight:700}
.pager{position:absolute;top:384px;left:0;width:100%;display:flex;justify-content:center;gap:8px;align-items:center}
.pager span{width:10px;height:10px;border-radius:50%;background:#c5ccd4}
.pager span.on{width:16px;height:16px;border:2px solid var(--blue);background:var(--white)}

/* footer */
.site-footer{top:3094px;height:399px;background:linear-gradient(180deg,var(--navy-2) 0%,var(--navy) 100%);color:#aab4c3}
.fcol{position:absolute;top:54px;width:235px;font-size:11px;line-height:17px}
.fcol h4{font-size:15px;font-weight:400;color:var(--white);text-transform:uppercase;letter-spacing:.5px;margin-bottom:18px}
.fcol ul{list-style:none;margin-top:14px}
.fcol li{font-size:10.5px;font-weight:700;color:var(--white);text-transform:uppercase;line-height:23px}
.fcol .item{margin-bottom:10px}
.fcol .item b{color:var(--white);font-weight:700;text-transform:uppercase}
.fcol .label{color:var(--white);font-weight:700;text-transform:uppercase;display:block;margin-top:6px}
.socials{display:flex;gap:8px}
.socials span{width:24px;height:24px;background:#3a4860}
.socials span.on{background:#1da1e0}
.footer-bottom{position:absolute;top:352px;left:87px;width:1026px;border-top:1px solid rgba(255,255,255,.08);padding-top:10px;display:flex;justify-content:space-between;font-size:10.5px;text-transform:uppercase;letter-spacing:.3px}
.footer-bottom nav{display:flex;gap:30px;color:#6d7a8f}
</style>
</head>
<body>

<header class="hero">
  <div class="photo hero-photo" role="img" aria-label="Photo of an oceanfront luxury resort with lawns, palm trees and a fountain terrace"></div>
  <nav class="main-nav">
    <a class="active">Welcome</a><a>Featured Listings</a><a>Previously Sold</a><a>Sell</a><a>Property Search</a><a>Team</a><a>Videos</a><a>Blog</a><a>Explore O.C.</a><a>Contact</a>
    <svg width="16" height="16" viewBox="0 0 16 16"><circle cx="6.5" cy="6.5" r="5" fill="none" stroke="#3a4657" stroke-width="1.6"/><line x1="10.2" y1="10.2" x2="14.5" y2="14.5" stroke="#3a4657" stroke-width="1.8"/></svg>
  </nav>
  <div class="brand-panel"><div class="brand-name">Marlow on the Shore</div></div>
  <div class="brand-tag">List with the Leader</div>
  <a class="hero-btn outline">Buy Your Home</a>
  <a class="hero-btn solid">Sell Your Home</a>
  <svg class="hero-arrow" width="40" height="40" viewBox="0 0 40 40"><polyline points="24,10 14,20 24,30" fill="none" stroke="#fff" stroke-width="2.5"/></svg>
  <div class="hero-dots"><span></span><span></span><span></span></div>
</header>

<section class="intro">
  <h2 class="section-title">List with the Leader</h2>
  <p>Lorem ipsum dolor sit amet, consectetuer adipiscing elit, sed diam nonummy nibh euismod tincidunt ut laoreet dolore magna aliquam erat volutpat. Ut wisi enim ad minim veniam, quis nostrud exerci tation ullamcorper suscipit lobortis nisl ut aliquip ex ea commodo consequat.</p>
  <p>Duis autem vel eum iriure dolor in hendrerit in vulputate velit esse molestie consequat, vel illum dolore eu feugiat nulla facilisis at vero eros et accumsan et iusto odio dignissim qui blandit praesent luptatum zzril delenit augue duis dolore te feugait nulla facilisi.</p>
  <a class="btn outline" style="left:374px;top:287px;width:220px">Contact Us</a>
  <a class="btn solid" style="left:604px;top:287px;width:219px">Meet the Team</a>
</section>

<section class="videos">
  <div class="photo videos-bg" role="img" aria-label="Photo of deep blue ocean with distant hills under a pale sky"></div>
  <h2 class="section-title">Marlow on the Shore Videos</h2>
  <svg class="side-arrow" style="left:30px;top:240px" width="20" height="34" viewBox="0 0 20 34"><polyline points="16,3 4,17 16,31" fill="none" stroke="#fff" stroke-width="2"/></svg>
  <svg class="side-arrow" style="right:30px;top:240px" width="20" height="34" viewBox="0 0 20 34"><polyline points="4,3 16,17 4,31" fill="none" stroke="#fff" stroke-width="2"/></svg>
  <div class="video" role="img" aria-label="Video still of an infinity pool with palm trees overlooking the sea" style="left:87px;top:142px;width:512px;height:295px;background:linear-gradient(180deg,#8cc4ec 0%,#6ab0de 40%,#2c96c8 65%,#9fd2e6 100%)">
    <svg width="66" height="66" viewBox="0 0 66 66"><circle cx="33" cy="33" r="30" fill="rgba(255,255,255,.15)" stroke="#fff" stroke-width="3"/><polygon points="26,20 48,33 26,46" fill="#fff"/></svg>
  </div>
  <div class="video" role="img" aria-label="Video still of a sunlit deck by the water" style="left:611px;top:142px;width:245px;height:142px;background:linear-gradient(180deg,#a6cde6,#4f8fb8 60%,#8a7a66)">
    <svg width="40" height="40" viewBox="0 0 40 40"><circle cx="20" cy="20" r="17" fill="none" stroke="#fff" stroke-width="2"/><polygon points="16,12 28,20 16,28" fill="#fff"/></svg>
  </div>
  <div class="video" role="img" aria-label="Video still of a bright living room with white sofas" style="left:866px;top:142px;width:247px;height:142px;background:linear-gradient(180deg,#e6e8ea,#c8ccd0 60%,#9a9690)">
    <svg width="40" height="40" viewBox="0 0 40 40"><circle cx="20" cy="20" r="17" fill="none" stroke="#fff" stroke-width="2"/><polygon points="16,12 28,20 16,28" fill="#fff"/></svg>
  </div>
  <div class="video" role="img" aria-label="Video still of a modern house lit at dusk" style="left:611px;top:295px;width:245px;height:142px;background:linear-gradient(180deg,#3b4f6e,#5a5a5c 55%,#c9924a)">
    <svg width="40" height="40" viewBox="0 0 40 40"><circle cx="20" cy="20" r="17" fill="none" stroke="#fff" stroke-width="2"/><polygon points="16,12 28,20 16,28" fill="#fff"/></svg>
  </div>
  <div class="video" role="img" aria-label="Video still of a poolside terrace at night" style="left:866px;top:295px;width:247px;height:142px;background:linear-gradient(180deg,#203a5e,#3d5a7c 50%,#2a8fb8)">
    <svg width="40" height="40" viewBox="0 0 40 40"><circle cx="20" cy="20" r="17" fill="none" stroke="#fff" stroke-width="2"/><polygon points="16,12 28,20 16,28" fill="#fff"/></svg>
  </div>
</section>

<section class="team">
  <h2 class="section-title">Meet the Team</h2>
  <svg class="side-arrow" style="left:30px;top:148px" width="16" height="30" viewBox="0 0 16 30"><polyline points="13,2 3,15 13,28" fill="none" stroke="#c8cdd3" stroke-width="2"/></svg>
  <svg class="side-arrow" style="right:30px;top:148px" width="16" height="30" viewBox="0 0 16 30"><polyline points="3,2 13,15 3,28" fill="none" stroke="#c8cdd3" stroke-width="2"/></svg>
  <div class="member" role="img" aria-label="Portrait of a team member" style="left:152px;top:135px;width:125px;height:125px;background:linear-gradient(180deg,#dfe3e7,#8996a6)"></div>
  <div class="member" role="img" aria-label="Portrait of a team member" style="left:302px;top:135px;width:125px;height:125px;background:linear-gradient(180deg,#e4e4e4,#6e5648)"></div>
  <div class="member" role="img" aria-label="Portrait of a team member" style="left:451px;top:135px;width:125px;height:125px;background:linear-gradient(180deg,#e8e6e4,#8a5a44)"></div>
  <div class="member" role="img" aria-label="Portrait of Nora Whitcombe, CEO Operations" style="left:601px;top:126px;width:147px;height:147px;border:4px solid #9fb9d8;background:linear-gradient(180deg,#7fa2c4,#c9a67c)"></div>
  <div class="member" role="img" aria-label="Portrait of a team member" style="left:771px;top:135px;width:125px;height:125px;background:linear-gradient(180deg,#ecebea,#b07050)"></div>
  <div class="member" role="img" aria-label="Portrait of a team member" style="left:922px;top:135px;width:125px;height:125px;background:linear-gradient(180deg,#6b4a3a,#3c3a3c)"></div>
  <div class="member-name"><strong>Nora Whitcombe</strong><span>CEO Operations</span></div>
</section>

<section class="listings">
  <h2 class="section-title">Featured Listings</h2>
  <div class="card" style="left:82px;top:132px"><div class="photo" role="img" aria-label="Photo of a villa with pool at dusk" style="background:linear-gradient(180deg,#2e4a70,#5a6f80 50%,#2c8ec0)"></div><div class="cap"><strong>Lorem Ipsum Dolor Sit</strong><span>Dana Point / Active</span></div></div>
  <div class="card" style="left:342px;top:132px"><div class="photo" role="img" aria-label="Photo of a bright living room facing the ocean" style="background:linear-gradient(180deg,#eef0f1,#c4cacf 60%,#8e8a84)"></div><div class="cap"><strong>Lorem Ipsum Dolor</strong><span>Dana Point / Active</span></div></div>
  <div class="card active" style="left:602px;top:132px"><div class="photo" role="img" aria-label="Photo of a glass-walled lounge at dusk" style="background:linear-gradient(180deg,#1d5f9c,#2c78b8 55%,#164a7d)"></div>
    <svg class="zoom" width="34" height="34" viewBox="0 0 34 34"><circle cx="14" cy="14" r="11" fill="none" stroke="#fff" stroke-width="2"/><line x1="22" y1="22" x2="31" y2="31" stroke="#fff" stroke-width="2.5"/><line x1="9" y1="14" x2="19" y2="14" stroke="#fff" stroke-width="2"/><line x1="14" y1="9" x2="14" y2="19" stroke="#fff" stroke-width="2"/></svg>
    <div class="cap"><strong>Lorem Ipsum Dolor Sit</strong><span>Dana Point / Active</span></div></div>
  <div class="card" style="left:862px;top:132px"><div class="photo" role="img" aria-label="Photo of a modern house with a lit pool" style="background:linear-gradient(180deg,#5b7896,#7d8a94 50%,#3a90b8)"></div><div class="cap"><strong>Lorem Ipsum Dolor</strong><span>Dana Point / Active</span></div></div>
  <div class="card" style="left:82px;top:387px"><div class="photo" role="img" aria-label="Photo of a terrace with loungers by the sea" style="background:linear-gradient(180deg,#7b98b8,#8f8f8a 55%,#3d7aa0)"></div><div class="cap"><strong>Lorem Ipsum Dolor Sit</strong><span>Dana Point / Active</span></div></div>
  <div class="card" style="left:342px;top:387px"><div class="photo" role="img" aria-label="Photo of a white lounge with sea views" style="background:linear-gradient(180deg,#dfe3e6,#b8bcbf 60%,#7e7a74)"></div><div class="cap"><strong>Lorem Ipsum Dolor</strong><span>Dana Point / Active</span></div></div>
  <div class="card" style="left:602px;top:387px"><div class="photo" role="img" aria-label="Photo of an open-plan living room" style="background:linear-gradient(180deg,#eceeee,#cfd1cf 60%,#9a958c)"></div><div class="cap"><strong>Lorem Ipsum Dolor Sit</strong><span>Dana Point / Active</span></div></div>
  <div class="card" style="left:862px;top:387px"><div class="photo" role="img" aria-label="Photo of a resort house with pool at twilight" style="background:linear-gradient(180deg,#2c3f66,#5c4f5a 50%,#2b9ac8)"></div><div class="cap"><strong>Lorem Ipsum Dolor</strong><span>Dana Point / Active</span></div></div>
  <a class="btn outline" style="left:489px;top:674px;width:220px;height:42px">Properties</a>
</section>

<section class="sold">
  <h2 class="section-title">Previously Sold</h2>
  <p>Duis autem vel eum iriure dolor in hendrerit in vulputate velit esse molestie consequat, vel illum dolore eu feugiat nulla facilisis at vero eros et accumsan et iusto odio dignissim qui blandit praesent luptatum zzril delenit augue duis dolore te feugait nulla facilisi.</p>
  <svg class="side-arrow" style="left:30px;top:256px" width="18" height="32" viewBox="0 0 18 32"><polyline points="15,2 4,16 15,30" fill="none" stroke="var(--blue)" stroke-width="2.5"/></svg>
  <svg class="side-arrow" style="right:30px;top:256px" width="18" height="32" viewBox="0 0 18 32"><polyline points="3,2 14,16 3,30" fill="none" stroke="#c8cdd3" stroke-width="2"/></svg>
  <div class="photo sold-item" role="img" aria-label="Photo of a sold villa with pool" style="left:87px;background:linear-gradient(180deg,#3e5674,#6d7680 50%,#2e88b4)"></div>
  <div class="photo sold-item" role="img" aria-label="Photo of a sold home's living room" style="left:345px;background:linear-gradient(180deg,#e6e8e9,#c0c4c6 60%,#8a857e)"></div>
  <div class="photo sold-item" role="img" aria-label="Photo of a sold home's glass lounge" style="left:603px;background:linear-gradient(180deg,#8a8f94,#5e6468 60%,#3e4246)">
    <svg style="position:absolute;left:105px;top:50px" width="34" height="34" viewBox="0 0 34 34"><circle cx="14" cy="14" r="11" fill="none" stroke="#fff" stroke-width="2"/><line x1="22" y1="22" x2="31" y2="31" stroke="#fff" stroke-width="2.5"/><line x1="9" y1="14" x2="19" y2="14" stroke="#fff" stroke-width="2"/><line x1="14" y1="9" x2="14" y2="19" stroke="#fff" stroke-width="2"/></svg>
    <div class="sold-over"><strong>Project Name</strong><span>View Details</span></div>
  </div>
  <div class="photo sold-item" role="img" aria-label="Photo of a sold resort home with pool" style="left:861px;width:252px;background:linear-gradient(180deg,#2e456c,#6a5660 50%,#2a9ccc)"></div>
  <div class="pager"><span></span><span class="on"></span><span></span><span></span><span></span></div>
</section>

<footer class="site-footer">
  <div class="fcol" style="left:87px">
    <h4>About MOS Realty</h4>
    <p>Ut wisi enim ad minim veniam, quis nostrud exerci tation ullamcorper suscipit lobortis nisl ut aliquip ex ea commodo consequat.</p>
    <ul><li>About Us</li><li>Our Blog</li><li>Our Services</li><li>Contact Us</li></ul>
  </div>
  <div class="fcol" style="left:347px">
    <h4>Blog Links</h4>
    <div class="item"><b>Item One</b> / 15 sep 2015.<br>Ut wisi enim ad nis nisl ut aliquip ex ea commodo consequat.</div>
    <div class="item"><b>Item Two</b> / 15 sep 2015.<br>Ut wisi enim ad nis nisl ut aliquip ex ea commodo consequat.</div>
    <div class="item"><b>Item Three</b> / 15 sep 2015.<br>Wisi enim ad nis nisl ut aliquip ex ea commodo consequat.</div>
  </div>
  <div class="fcol" style="left:604px">
    <h4>Contact Us</h4>
    <span class="label">Address:</span>Marlow on the Shore<br>Harbor Lane, Laguna, USA
    <span class="label">Sales :</span>Sales Telephone No : 555 0142 0198<br>Sales Email Account : sales@marlowshore.example
    <span class="label">Support :</span>Support Telephone No : 555 0142 0177<br>Support Email Account : support@marlowshore.example
  </div>
  <div class="fcol" style="left:863px">
    <h4>Connect With Us</h4>
    <div class="socials" aria-label="Social links"><span></span><span class="on"></span><span></span><span></span><span></span></div>
  </div>
  <div class="footer-bottom"><span>Copyright © 2015. Marlow on the Shore Inc. All rights reserved.</span><nav><span>Terms of Use</span><span>Privacy Policy</span></nav></div>
</footer>

</body>
</html>
```